Packaging design for high end, natural skin care line needed

Marisol Thackery Beauty needs a label design. It is a new skin care line I am launching.
For years my line Velvet Orchard Beauty was quite popular and featured in several magazines, but for personal reasons had to be shut down. Now I am launching a new line featuring VOB's top selling products, but focused solely on skin care more so than cosmetics. All products will still be handmade, but the line should still look professional-something worthy of a Brindle Market shelf!
I am branding it with my name, as I am often quoted in articles related to gluten in beauty products, so Marisol Thackery and beauty are key words.
The key products will be facial and body serums which are packaged in .5oz., 1oz. and larger amber glass bottles with black dropper tops, I will include pictures below. For dimensions, the labels can be any size that you think will work best, but need to at the least fit the 1oz. bottle, dimensions shown here http://www.corvelflask.example/amber-glass-tall-round-flask/p/QZ7K-93/
I loved the former VOB logo, but for Marisol Thackery Beauty I am looking for something more personal, more apothecary-like, and probably less colorful.
The line will be small, just a handful of products, but luxe, rich.
I am attaching photos of Velvet Orchard Beauty's packaging for your reference.
Thanks much!!

Hi Everyone! Thank you for your submissions! Please see the links I provided in the brief, I really am looking for something more technical looking, like an apothecary. And want black text on a white background, not a black background, and nothing flowery.
Thank you all!!
Marisol

Target Market(s)

My clients are primarily women of all ages, but with more of a skin care focus, and no longer a cosmetic one, I would also like to appeal to a male audience. My clients are health conscious, gluten-free, natural, paleo, or vegan, etc. Target age is probably 25-55. Products are a bit high end, priced $45-65.

Industry/Entity Type

Cosmetics

Requirements
Must have
• It must at least say Marisol Thackery, or can say Marisol Thackery Beauty, but "Beauty" is not necessary. And capitalization is open, try whatever you think serves the brand. Likely slogans or taglines that can be included but are not essential: Care for your skin. Love and care for your skin. Handmade with love in the USA. Handmade in the USA. Think modern day apothecary. Small batch scotch. Something fine, but custom, handmade.
Nice to have
• I like the aesthetic of Oribel Skin Care a bit http://www.oribelhollis.example.au/
And of Dorian Valtz as shown here http://www.pinboardia.example/pin/847302915563017442/
Also of something like this that is even customizable http://www.pinboardia.example/pin/58274106392285514/
Every product is handmade in small batches, with fine ingredients, a moderate price point of around $45-$65. And I will likely begin making custom orders. So there could be a space to say when it was made, or for whom. I would like to keep the colors classic though, I probably want to stay away from the bright pink on this one.
Should not have
• As I mentioned, probably want to stay away from a lot of color. I like black vs. gray for the text, as it will show up better in editorials. I must look good, but also photograph well. Thanks!

```html
<!DOCTYPE html>
<html lang="en">
<head>
<meta charset="utf-8">
<title>Marisol Thackery Beauty – Serum Label</title>
<link rel="stylesheet" href="https://fonts.googleapis.com/css2?family=Courier+Prime&family=Noto+Sans:wght@400&display=swap">
<style>
  :root {
    --page: #fefefe;
    --brown: #7b4b3e;
    --teal: #4aa3ad;
    --label-edge: #ebebeb;
    --label-edge-right: #e4e5e7;
    --label-center: #ffffff;
  }
  * { box-sizing: border-box; margin: 0; padding: 0; }
  html, body {
    width: 1200px;
    height: 824px;
    overflow: hidden;
    background: var(--page);
  }
  .canvas {
    position: relative;
    width: 1200px;
    height: 824px;
    border-bottom: 1px solid #e6e6e6;
  }
  .label {
    position: absolute;
    left: 192px;
    top: 202px;
    width: 806px;
    height: 460px;
    background: linear-gradient(to right, var(--label-edge) 0%, var(--label-center) 45%, var(--label-center) 55%, var(--label-edge-right) 100%);
  }
  .label__band {
    position: absolute;
    left: 0;
    width: 100%;
    height: 12px;
    background: var(--brown);
  }
  .label__band--top { top: 0; }
  .label__band--bottom { bottom: 0; }

  .tagline {
    position: absolute;
    top: 61px;
    left: 0;
    width: 806px;
    text-align: center;
    font-family: "Courier Prime", monospace;
    font-size: 13px;
    color: var(--teal);
  }
  .brand {
    position: absolute;
    top: 270px;
    left: 0;
    width: 810px;
    text-align: center;
  }
  .brand__name {
    font-family: "Noto Sans", sans-serif;
    font-weight: 400;
    font-size: 46px;
    color: var(--brown);
    line-height: 56px;
  }
  .brand__sub {
    position: absolute;
    left: 338px;
    top: 62px;
    font-family: "Noto Sans", sans-serif;
    font-size: 22px;
    letter-spacing: 4px;
    color: var(--teal);
  }
  .brand__mark {
    position: absolute;
    left: 440px;
    top: 66px;
    width: 64px;
    height: 46px;
    border-radius: 50% 60% 45% 55%;
    background: radial-gradient(ellipse at 40% 45%, #5fb2ba 0%, #8fcad0 60%, rgba(143,202,208,0) 100%);
  }

  .custom-box {
    position: absolute;
    left: 702px;
    top: 29px;
    width: 93px;
    height: 388px;
    border: 2px solid var(--brown);
  }
  .custom-box__rule {
    position: absolute;
    left: 44px;
    top: 9px;
    width: 2px;
    height: 368px;
    background: var(--brown);
  }
  .custom-box__field {
    position: absolute;
    top: 8px;
    height: 364px;
    width: 26px;
    writing-mode: vertical-rl;
    transform: rotate(180deg);
    font-family: "Courier Prime", monospace;
    font-size: 20px;
    letter-spacing: 2.5px;
    color: var(--brown);
    white-space: nowrap;
  }
  .custom-box__field--made { left: 12px; }
  .custom-box__field--for { left: 55px; }
</style>
</head>
<body>
  <main class="canvas">
    <section class="label">
      <div class="label__band label__band--top"></div>
      <p class="tagline">Handmade in the USA</p>
      <div class="brand">
        <h1 class="brand__name">Marisol Thackery</h1>
        <span class="brand__sub">beauty</span>
        <div class="brand__mark" role="img" aria-label="Small teal stippled almond illustration"></div>
      </div>
      <div class="custom-box">
        <div class="custom-box__field custom-box__field--made">Made: 15.01.2014</div>
        <div class="custom-box__rule"></div>
        <div class="custom-box__field custom-box__field--for">For: Odette Varnell</div>
      </div>
      <div class="label__band label__band--bottom"></div>
    </section>
  </main>
</body>
</html>
```